Business Card Design

Please see my website www.qvlearnix.com.au to for further information on my services and styling of my site

Reason: Deadline is extended to permit alterations to current designs or for any new submissions. Cheers

Industry/Entity Type

Business

Contact Information for Business Card

Marcus Pelton
Empowerment Coach

'Live your passion'

marcus@qvlearnix.com.au
0438157264
qvlearnix.com.au

```html
<!DOCTYPE html>
<html lang="en">
<head>
<meta charset="utf-8">
<title>QV Learnix Coaching – Business Card</title>
<link rel="stylesheet" href="https://fonts.googleapis.com/css2?family=Oswald:wght@500&family=Fira+Sans:wght@400&display=swap">
<style>
  :root {
    --page: #ffffff;
    --charcoal: #37323a;
    --lime: #b9d433;
    --green-deep: #8cc540;
    --green-light: #bcd63a;
    --ink: #1f2620;
    --white: #ffffff;
    --silver: #b8b9bc;
  }
  * { margin: 0; padding: 0; box-sizing: border-box; }
  html, body {
    width: 1200px; height: 1000px; overflow: hidden;
    background: var(--page);
  }
  .canvas { position: relative; width: 1200px; height: 1000px; }
  .card {
    position: absolute; left: 280px; width: 623px; height: 384px; overflow: hidden;
  }

  /* Front */
  .card--front { top: 79px; background: var(--charcoal); }
  .front__band {
    position: absolute; left: 0; right: 0; top: 324px; bottom: 0;
    background: linear-gradient(90deg, var(--green-deep), var(--green-light));
  }
  .front__figures {
    position: absolute; left: 395px; top: 116px; width: 170px; height: 208px;
    background: linear-gradient(90deg, var(--silver) 0%, var(--silver) 35%, var(--lime) 36%, var(--lime) 100%);
    border-radius: 60px 60px 0 0;
    opacity: .9;
  }
  .front__mark {
    position: absolute; left: 312px; top: 62px;
    font-family: "Oswald", sans-serif; font-weight: 500;
    font-size: 62px; line-height: 1; color: var(--lime); letter-spacing: 2px;
  }
  .front__name {
    position: absolute; left: 48px; top: 280px;
    font-family: "Oswald", sans-serif; font-weight: 500;
    font-size: 25px; line-height: 1; color: var(--white);
  }

  /* Back */
  .card--back {
    top: 541px;
    background: linear-gradient(135deg, var(--green-deep) 0%, #96c83c 55%, var(--green-light) 100%);
  }
  .back__figures {
    position: absolute; left: 250px; top: 0; width: 373px; height: 384px;
    background: radial-gradient(ellipse at 55% 45%, rgba(120,185,70,.55), rgba(120,185,70,0) 70%);
  }
  .back__logo { position: absolute; left: 45px; top: 50px; width: 265px; }
  .back__mark {
    display: flex; align-items: center; gap: 14px;
    font-family: "Oswald", sans-serif; font-weight: 500;
    font-size: 62px; line-height: 1; color: var(--white); letter-spacing: 2px;
  }
  .back__mark-square { width: 34px; height: 34px; background: var(--charcoal); }
  .back__rule { margin-top: 18px; height: 4px; background: var(--charcoal); }
  .back__name {
    margin-top: 10px;
    font-family: "Oswald", sans-serif; font-weight: 500;
    font-size: 25px; line-height: 1; color: var(--charcoal);
  }
  .contact {
    position: absolute; left: 367px; top: 186px;
    font-family: "Fira Sans", sans-serif; font-weight: 400; color: var(--ink);
  }
  .contact__name { font-size: 23px; line-height: 28px; }
  .contact__line { font-size: 17px; line-height: 22px; }
  .contact__gap { height: 22px; }
</style>
</head>
<body>
<main class="canvas">
  <section class="card card--front">
    <div class="front__band"></div>
    <div class="front__figures" role="img" aria-label="Silhouettes of two people raising their arms in celebration"></div>
    <div class="front__mark">QVL</div>
    <div class="front__name">QV Learnix Coaching</div>
  </section>

  <section class="card card--back">
    <div class="back__figures" role="img" aria-label="Large faint silhouettes of people with raised arms"></div>
    <div class="back__logo">
      <div class="back__mark">QVL <span class="back__mark-square"></span></div>
      <div class="back__rule"></div>
      <div class="back__name">QV Learnix Coaching</div>
    </div>
    <div class="contact">
      <div class="contact__name">Marcus Pelton</div>
      <div class="contact__line">Empowerment Coach</div>
      <div class="contact__line">'Live your passion'</div>
      <div class="contact__gap"></div>
      <div class="contact__line">marcus@qvlearnix.com.au</div>
      <div class="contact__line">0438157264</div>
      <div class="contact__line">www.qvlearnix.com.au</div>
    </div>
  </section>
</main>
</body>
</html>
```